Layout for site fence advertising - length approx. 250 cm x 125 cm

The advertising will later be printed on a PVC film and used for events or on sports fields.

Main services :
Your regional contact at
Real estate and business financing
independent insurance advice

```html
<!DOCTYPE html>
<html lang="de">
<head>
<meta charset="utf-8">
<title>RM Finanzberatung – Bauzaunbanner</title>
<link rel="stylesheet" href="https://fonts.googleapis.com/css2?family=Quicksand:wght@500;700&family=Teko:wght@500;600&display=swap">
<style>
  :root {
    --brand-blue: #1a56bb;
    --slate-grey: #5f5f5f;
    --ink-grey: #4a4a4a;
    --paper: #ffffff;
    --stage: #3c3c3c;
    --photo-dark: #3b2a26;
    --photo-mid: #8a6a5c;
    --photo-light: #d9d2cc;
  }
  * { margin: 0; padding: 0; box-sizing: border-box; }
  html, body {
    width: 1000px;
    height: 1200px;
    overflow: hidden;
    background: var(--stage);
  }
  .banner {
    position: absolute;
    left: 20px;
    top: 360px;
    width: 960px;
    height: 480px;
    background: var(--paper);
    overflow: hidden;
    box-shadow: 0 10px 40px rgba(0,0,0,0.45);
  }
  .banner-shapes {
    position: absolute;
    inset: 0;
  }
  .brand {
    position: absolute;
    left: 36px;
    top: 36px;
    height: 122px;
    display: flex;
    align-items: center;
  }
  .brand-dot {
    width: 116px;
    height: 116px;
    border: 4px solid var(--brand-blue);
    border-radius: 50%;
    flex: none;
  }
  .brand-divider {
    width: 3px;
    height: 122px;
    background: var(--slate-grey);
    margin: 0 10px 0 14px;
  }
  .brand-text { margin-top: 10px; }
  .brand-name {
    font-family: "Quicksand", sans-serif;
    font-weight: 700;
    font-size: 23px;
    color: var(--brand-blue);
    line-height: 1.1;
  }
  .brand-tagline {
    font-family: "Quicksand", sans-serif;
    font-weight: 500;
    font-size: 16px;
    color: var(--ink-grey);
    margin-top: 4px;
  }
  .services {
    position: absolute;
    left: 36px;
    top: 200px;
    color: var(--paper);
    font-family: "Teko", sans-serif;
    text-transform: uppercase;
  }
  .services-title {
    font-weight: 600;
    font-size: 46px;
    letter-spacing: 3px;
    line-height: 1;
    margin-bottom: 12px;
  }
  .services-list { list-style: none; }
  .services-list li {
    font-weight: 500;
    font-size: 28px;
    letter-spacing: 0.6px;
    line-height: 35px;
  }
  .services-list li::before {
    content: "";
    display: inline-block;
    width: 9px;
    height: 9px;
    border-radius: 50%;
    background: var(--paper);
    margin-right: 7px;
    vertical-align: 5px;
  }
  .website {
    position: absolute;
    left: 36px;
    top: 426px;
    max-width: 470px;
    white-space: nowrap;
    font-family: "Teko", sans-serif;
    font-weight: 600;
    font-size: 36px;
    letter-spacing: 4px;
    color: var(--paper);
    line-height: 1;
    text-transform: uppercase;
  }
</style>
</head>
<body>
  <main class="banner">
    <svg class="banner-shapes" width="960" height="480" viewBox="0 0 960 480">
      <defs>
        <linearGradient id="portrait-tones" x1="0" y1="0" x2="1" y2="1">
          <stop offset="0" stop-color="#3b2a26"/>
          <stop offset="0.45" stop-color="#8a6a5c"/>
          <stop offset="1" stop-color="#d9d2cc"/>
        </linearGradient>
      </defs>
      <polygon class="services-band" points="0,170 576,170 518,413 0,413" fill="#1a56bb"/>
      <polygon class="web-band" points="0,413 532,413 516,480 0,480" fill="#5f5f5f"/>
      <polygon class="accent-stripe-blue" points="664,0 672,0 524,412 518,412" fill="#1a56bb"/>
      <polygon class="accent-stripe-grey" points="606,205 612,205 538,412 528,412" fill="#5f5f5f"/>
      <polygon class="portrait" points="674,0 960,0 960,480 541,480" fill="url(#portrait-tones)" role="img" aria-label="Porträtfoto des Beraters im dunklen Sakko und weißen Hemd"/>
    </svg>

    <header class="brand">
      <span class="brand-dot"></span>
      <span class="brand-divider"></span>
      <div class="brand-text">
        <div class="brand-name">RM Finanzberatung GmbH</div>
        <div class="brand-tagline">Finanzieren, Versichern, Vorsorgen</div>
      </div>
    </header>

    <section class="services">
      <h2 class="services-title">Main Services :</h2>
      <ul class="services-list">
        <li>Your regional contact at</li>
        <li>Real estate and business financing</li>
        <li>Independent insurance advice</li>
      </ul>
    </section>

    <p class="website">www.rmfinanz.example</p>
  </main>
</body>
</html>
```